Design für Geburtsanzeigekarte DIN Lang
Zielgruppe
Ich bin Fotograf und habe mich auf Schwangerschafts- und Neugeborenenfotografie spezialisiert. Meine Zielgruppe sind schwangere Frauen im letzten Drittel der Schwangerschaft und frisch gewordene Eltern.
Aufgabenstellung
- Referenzdesign finden Sie als Anlage zu dieser Ausschreibung, die Karten haben wir schon damit Sie aber sehen was ich mir vorstelle
- Lieferung als offene Indesign Datei (so das die Farben, Texte, .... angepasst werden können)
- 2-3 Bilder sollen in das Design eingearbeitet werden können
- Die Karten werden von mir nachher als fertig gedruckte Karte an meine Kunden verkauft, dies bitte ich zu berücksichtigen
- ich möchte die Karten so nutzen können das sowohl Geburtskarten für Jungs wie auch für Mädels erstellt werden können
- Format: DIN Lang (210x100mm), Klappkarte, quer, 3mm Beschnitt
- Schriften sollten mitgeliefert werden oder aus Quellen stammen wo sie kostenfrei auch für kommerzielle Zwecke genutzt werden können

```html
<!DOCTYPE html>
<html lang="de">
<head>
<meta charset="utf-8">
<title>Geburtsanzeige DIN Lang – Klappkarte</title>
<link href="https://fonts.googleapis.com/css2?family=Amatic+SC:wght@700&family=Dancing+Script:wght@600&family=Oswald:wght@300;400&family=Roboto+Condensed:wght@300&display=swap" rel="stylesheet">
<style>
  :root {
    --bg: #eef1ea;
    --blue: #9fb0c0;
    --mauve: #857d8c;
    --white: #ffffff;
    --ink-soft: #8a93a0;
    --skin-light: #f2e3da;
    --skin-mid: #e6c9b8;
    --fur: #efe4da;
  }
  * { margin: 0; padding: 0; box-sizing: border-box; }
  html, body { width: 777px; height: 1200px; overflow: hidden; background: var(--bg); }
  .canvas { position: relative; width: 777px; height: 1200px; }

  .spread { position: absolute; left: 12px; width: 753px; height: 197px; overflow: hidden; background: var(--white); }
  .spread--outside { top: 380px; }
  .spread--inside { top: 623px; }

  .photo { position: absolute; }
  .photo--hands { left: 0; top: 0; width: 187px; height: 125px;
    background: radial-gradient(circle at 45% 55%, #f0cdbf 0%, #e3b8a6 35%, #d9c9c2 75%); }
  .photo--feet-heart { left: 374px; top: 0; width: 164px; height: 125px;
    background: radial-gradient(circle at 50% 50%, #f1d2c5 0%, #e2c0ad 40%, #f4f0ec 85%); }
  .photo--sleeping-baby { left: 538px; top: 0; width: 215px; height: 197px;
    background: radial-gradient(ellipse at 55% 25%, #f1e9ee 0%, #eadde0 22%, transparent 23%),
                radial-gradient(ellipse at 50% 65%, var(--skin-mid) 0%, var(--skin-light) 45%, var(--fur) 80%); }
  .photo--smiling-baby { left: 0; top: 0; width: 376px; height: 197px;
    background: radial-gradient(ellipse at 48% 55%, #f0d5c3 0%, #ead3c2 35%, #f3ece2 70%, #f6f2ea 100%); }

  .quote { position: absolute; left: 187px; top: 0; width: 187px; height: 125px;
    text-align: center; color: var(--ink-soft); }
  .quote__small { font-family: 'Oswald', sans-serif; font-weight: 300; font-size: 12px; letter-spacing: .5px;
    position: absolute; left: 0; right: 0; top: 8px; padding-left: 50px; }
  .quote__script { font-family: 'Dancing Script', cursive; font-size: 52px; line-height: 1;
    position: absolute; left: 0; right: 0; top: 22px; color: var(--blue); }
  .quote__line { font-family: 'Oswald', sans-serif; font-weight: 300; font-size: 13px; color: var(--mauve);
    position: absolute; left: 0; right: 0; top: 72px; }
  .quote__last { position: absolute; left: 0; right: 0; top: 92px; font-size: 16px; }
  .quote__pill { display: inline-block; background: var(--blue); color: var(--white); border-radius: 10px;
    font-family: 'Oswald', sans-serif; font-weight: 300; font-size: 10px; padding: 1px 7px; vertical-align: middle; }
  .quote__sein { font-family: 'Dancing Script', cursive; color: var(--mauve); font-size: 17px; vertical-align: middle; }

  .band { position: absolute; left: 0; top: 125px; width: 538px; height: 72px; background: var(--blue); }
  .title { position: absolute; top: 0; height: 72px; display: flex; flex-direction: column; align-items: center; justify-content: center; }
  .title--thanks { left: 0; width: 374px; }
  .title--name { left: 374px; width: 164px; }
  .title__text { font-family: 'Amatic SC', sans-serif; font-weight: 700; color: var(--white); font-size: 36px; letter-spacing: 1px; line-height: 1; margin: 4px 0; }
  .title__rule { width: 100px; height: 2px; background: var(--mauve); border-radius: 1px; }

  .ring { position: absolute; left: 0; top: 0; width: 100%; height: 100%; display: block; }

  .badge { position: absolute; }
  .badge--miracle { left: 501px; top: 81px; width: 74px; height: 74px; }
  .badge__label { position: absolute; inset: 0; display: flex; flex-direction: column; align-items: center; justify-content: center;
    font-family: 'Amatic SC', sans-serif; font-weight: 700; color: var(--blue); font-size: 16px; line-height: .95; text-align: center; }

  .details { position: absolute; left: 376px; top: 0; width: 377px; height: 197px; background: var(--white); }
  .details__band { position: absolute; left: 0; top: 0; width: 100%; height: 38px; background: var(--blue); }
  .details__foot { position: absolute; left: 0; bottom: 0; width: 100%; height: 3px; background: var(--blue); }
  .fact { position: absolute; top: 37px; width: 63px; height: 63px; }
  .fact--date { left: 38px; }
  .fact--time { left: 119px; }
  .fact--weight { left: 200px; }
  .fact--length { left: 281px; }
  .fact__content { position: absolute; inset: 0; display: flex; flex-direction: column; align-items: center; justify-content: center;
    font-family: 'Amatic SC', sans-serif; font-weight: 700; color: var(--mauve); font-size: 12px; line-height: .95; text-align: center; }
  .fact__icon { width: 14px; height: 12px; margin-bottom: 2px; display: block; }
  .details__heading { position: absolute; left: 0; right: 0; top: 111px; text-align: center;
    font-family: 'Amatic SC', sans-serif; font-weight: 700; color: var(--mauve); font-size: 18px; letter-spacing: .5px; }
  .details__text { position: absolute; left: 60px; right: 60px; top: 140px; text-align: center;
    font-family: 'Roboto Condensed', sans-serif; font-weight: 300; color: var(--ink-soft); font-size: 5.6px; line-height: 8px; }
</style>
</head>
<body>
<svg width="0" height="0" style="position:absolute" aria-hidden="true">
  <defs>
    <symbol id="scallop-badge" viewBox="0 0 100 100">
      <circle cx="50" cy="50" r="50" fill="#857d8c"/>
      <g fill="#ffffff">
        <circle cx="50" cy="50" r="38"/>
        <circle cx="50" cy="11" r="6"/><circle cx="64.9" cy="14" r="6"/><circle cx="77.6" cy="22.4" r="6"/><circle cx="86" cy="35.1" r="6"/>
        <circle cx="89" cy="50" r="6"/><circle cx="86" cy="64.9" r="6"/><circle cx="77.6" cy="77.6" r="6"/><circle cx="64.9" cy="86" r="6"/>
        <circle cx="50" cy="89" r="6"/><circle cx="35.1" cy="86" r="6"/><circle cx="22.4" cy="77.6" r="6"/><circle cx="14" cy="64.9" r="6"/>
        <circle cx="11" cy="50" r="6"/><circle cx="14" cy="35.1" r="6"/><circle cx="22.4" cy="22.4" r="6"/><circle cx="35.1" cy="14" r="6"/>
      </g>
    </symbol>
  </defs>
</svg>

<main class="canvas">
  <section class="spread spread--outside" aria-label="Kartenaußenseite">
    <div class="photo photo--hands" role="img" aria-label="Foto: Babyhand in Elternhand"></div>
    <div class="quote">
      <div class="quote__small">GROSSES</div>
      <div class="quote__script">Glück</div>
      <div class="quote__line">~ KANN SO ~</div>
      <div class="quote__last"><span class="quote__pill">KLEIN</span> <span class="quote__sein">Sein!</span></div>
    </div>
    <div class="photo photo--feet-heart" role="img" aria-label="Foto: Babyfüße in Herzform von Elternhänden gehalten"></div>
    <div class="photo photo--sleeping-baby" role="img" aria-label="Foto: schlafendes Neugeborenes mit Strickmütze auf Fell"></div>
    <div class="band">
      <div class="title title--thanks">
        <div class="title__rule"></div>
        <div class="title__text">DANKE!</div>
        <div class="title__rule"></div>
      </div>
      <div class="title title--name">
        <div class="title__rule"></div>
        <div class="title__text">LiNA</div>
        <div class="title__rule"></div>
      </div>
    </div>
    <div class="badge badge--miracle">
      <svg class="ring" viewBox="0 0 100 100"><use href="#scallop-badge"/></svg>
      <div class="badge__label"><span>EiN</span><span>WUNDER</span></div>
    </div>
  </section>

  <section class="spread spread--inside" aria-label="Karteninnenseite">
    <div class="photo photo--smiling-baby" role="img" aria-label="Foto: lächelndes Baby auf hellem Hintergrund"></div>
    <div class="details">
      <div class="details__band"></div>
      <div class="fact fact--date">
        <svg class="ring" viewBox="0 0 100 100"><use href="#scallop-badge"/></svg>
        <div class="fact__content">
          <svg class="fact__icon" viewBox="0 0 14 12" fill="none" stroke="#857d8c" stroke-width="1"><rect x="1" y="2" width="12" height="9" rx="1"/><line x1="1" y1="5" x2="13" y2="5"/><line x1="4" y1="0.5" x2="4" y2="3"/><line x1="10" y1="0.5" x2="10" y2="3"/></svg>
          <span>10.02.</span><span>2018</span>
        </div>
      </div>
      <div class="fact fact--time">
        <svg class="ring" viewBox="0 0 100 100"><use href="#scallop-badge"/></svg>
        <div class="fact__content">
          <svg class="fact__icon" viewBox="0 0 14 12" fill="none" stroke="#857d8c" stroke-width="1"><circle cx="7" cy="6" r="5"/><polyline points="7,3 7,6 9,7"/></svg>
          <span>18:15</span><span>UHR</span>
        </div>
      </div>
      <div class="fact fact--weight">
        <svg class="ring" viewBox="0 0 100 100"><use href="#scallop-badge"/></svg>
        <div class="fact__content">
          <svg class="fact__icon" viewBox="0 0 14 12" fill="none" stroke="#857d8c" stroke-width="1"><path d="M2 8 h10 l-1 3 h-8 z"/><circle cx="7" cy="4" r="2.5"/></svg>
          <span>3000</span><span>G</span>
        </div>
      </div>
      <div class="fact fact--length">
        <svg class="ring" viewBox="0 0 100 100"><use href="#scallop-badge"/></svg>
        <div class="fact__content">
          <svg class="fact__icon" viewBox="0 0 14 12" fill="none" stroke="#857d8c" stroke-width="1"><ellipse cx="7" cy="5" rx="5" ry="3.5"/><circle cx="7" cy="5" r="1.2"/><path d="M12 5 v5 h-4"/></svg>
          <span>52</span><span>CM</span>
        </div>
      </div>
      <h2 class="details__heading">ViELEN DANK!</h2>
      <p class="details__text">Wir danken allen von Herzen für die lieben Grüße, Glückwünsche und Geschenke zur Geburt unserer Tochter. Jede Karte, jeder Anruf und jeder Besuch hat uns in den ersten Wochen viel Freude bereitet. Wir genießen jeden Tag mit unserem kleinen Wunder. Herzliche Grüße von uns allen. Eure Familie</p>
      <div class="details__foot"></div>
    </div>
  </section>
</main>
</body>
</html>
```